Tarrendale Secondary College House displays

Our school has 4 new houses that are designed to promote school connectedness and school pride. Each house display should include the name of the house, a silhouette portrait of the person the house is named after and a famous quote from that person. Each house display should also promote the unique house colour. Details are included in the attached word document. I have also attached a Marcus Threlby poster that gives some sort of idea about the look and feel we are after. The house name should be quite prominent.

Target Market(s)

Tarrendale Secondary College has 1800 students. We are a unique school committed to a strengths based program. Our house system is designed to connect students to each other and to the school. To understand our school visit our website at www.tarrendalesc.vic.edu.au

Logo Text

We want a logo for each of our houses that has the house name on it - see the attached word document for details.

Font styles to use
Sans Serif

Colors
0792cd
00a990
fbed22
ec1f27

Requirements
Must have
• Colour- each house must include the colour it is aligned to. This is outlined in the attached word document

```html
<!DOCTYPE html>
<html lang="en">
<head>
<meta charset="utf-8">
<title>Tarrendale Secondary College – House Displays</title>
<link href="https://fonts.googleapis.com/css2?family=Poppins:wght@300;400;600;700;800;900&display=swap" rel="stylesheet">
<style>
  :root {
    --navy: #040f2b;
    --house-blue: #0792cd;
    --house-yellow: #fbed22;
    --house-green: #00a990;
    --house-red: #ec1f27;
    --ink: #1c1a14;
    --paper: #ffffff;
    --pale-yellow: #fdf27a;
    --ring-yellow: #f7e21a;
  }
  * { margin: 0; padding: 0; box-sizing: border-box; }
  html, body { width: 1200px; height: 624px; overflow: hidden; background: var(--paper); }
  body { position: relative; font-family: "Poppins", sans-serif; }

  .house-poster {
    position: absolute;
    top: 19px;
    height: 580px;
    overflow: hidden;
  }
  .house-poster--varley { left: 19px; width: 580px; background: var(--navy); color: var(--paper); }
  .house-poster--talo { left: 613px; width: 567px; background: var(--house-yellow); color: var(--ink); }

  .house-name {
    position: absolute;
    font-weight: 900;
    line-height: 1;
    white-space: nowrap;
    -webkit-background-clip: text;
    background-clip: text;
    color: transparent;
  }
  .house-label {
    position: absolute;
    writing-mode: vertical-rl;
    font-weight: 800;
    line-height: 1;
  }

  /* Varley */
  .accent-square {
    position: absolute;
    left: 280px; top: 40px;
    width: 82px; height: 104px;
    background: var(--house-blue);
    transform: rotate(9deg);
  }
  .house-poster--varley .house-name {
    left: 46px; top: 42px;
    font-size: 114px;
    letter-spacing: -2px;
    background-image: linear-gradient(180deg, #e6e4d6 0%, #cfcdb4 45%, #a9ab8a 100%);
  }
  .house-poster--varley .house-label {
    left: 504px; top: 49px;
    width: 27px; height: 86px;
    background: var(--house-blue);
    color: var(--navy);
    font-size: 22px;
    text-align: center;
    padding-top: 3px;
  }
  .corner-disc { position: absolute; border-radius: 50%; }
  .corner-disc--blue { left: -150px; top: 450px; width: 290px; height: 290px; background: var(--house-blue); }

  .portrait { position: absolute; }
  .portrait--varley {
    left: 290px; top: 150px; width: 290px; height: 430px;
    background:
      radial-gradient(ellipse 32% 26% at 46% 26%, rgba(226,214,196,.95), transparent 70%),
      radial-gradient(ellipse 45% 30% at 70% 40%, rgba(40,110,160,.7), transparent 70%),
      radial-gradient(ellipse 40% 22% at 55% 80%, rgba(190,40,50,.75), transparent 70%),
      radial-gradient(ellipse 50% 40% at 80% 70%, rgba(70,120,60,.6), transparent 70%),
      radial-gradient(ellipse 55% 45% at 40% 50%, rgba(60,70,130,.6), transparent 75%);
  }
  .quote { position: absolute; font-weight: 400; }
  .quote strong { font-weight: 700; }
  .quote-mark { font-weight: 700; line-height: 1; }

  .quote--varley {
    left: 49px; top: 170px;
    font-size: 27px; line-height: 29px;
    letter-spacing: -0.2px;
  }
  .quote--varley .quote-lead { font-size: 31px; font-weight: 700; display: block; line-height: 34px; }
  .quote--varley .quote-mark { position: absolute; left: -33px; top: 2px; font-size: 46px; }
  .quote--varley .quote-close { display: inline-block; font-size: 46px; vertical-align: top; line-height: 1; margin-left: 4px; margin-top: -6px; }

  .bio { position: absolute; font-weight: 300; }
  .bio strong { font-weight: 700; }
  .bio--varley { left: 377px; top: 424px; width: 186px; color: var(--paper); font-size: 9px; line-height: 11.2px; }

  /* Talo */
  .house-poster--talo .house-name {
    left: 40px; top: 31px;
    font-size: 160px;
    letter-spacing: -5px;
    background-image: linear-gradient(180deg, #6d7474 0%, #8b8478 30%, #7a3e22 55%, #5b4a28 75%, #3f3c22 100%);
  }
  .house-name .ringed-letter { position: relative; }
  .house-name .ringed-letter::after {
    content: "";
    position: absolute;
    left: 50%; top: 39%;
    width: 0.72em; height: 0.72em;
    transform: translate(-50%, -50%);
    border-radius: 50%;
    border: 5px solid var(--ring-yellow);
    box-shadow: 0 0 0 2px rgba(255,250,160,.6);
  }
  .house-poster--talo .house-label {
    left: 510px; top: 55px;
    font-size: 25px;
    color: var(--ink);
  }
  .corner-disc--yellow { left: -72px; top: 415px; width: 250px; height: 250px; background: var(--pale-yellow); opacity: .8; }
  .small-disc { position: absolute; border-radius: 50%; }
  .small-disc--dark { left: 472px; top: 200px; width: 19px; height: 19px; background: #222; }
  .small-disc--teal { left: 480px; top: 177px; width: 16px; height: 16px; background: #3aa79c; }
  .small-disc--white { left: 529px; top: 184px; width: 12px; height: 12px; background: #fff9c8; }
  .small-disc--edge { left: 550px; top: 302px; width: 40px; height: 40px; background: #1a1a1a; }
  .small-disc--soft { left: 154px; top: 501px; width: 35px; height: 35px; background: var(--pale-yellow); }

  .portrait--talo {
    left: 270px; top: 170px; width: 290px; height: 320px;
    background:
      radial-gradient(ellipse 30% 32% at 45% 45%, rgba(150,110,30,.9), transparent 72%),
      radial-gradient(ellipse 40% 30% at 80% 30%, rgba(245,140,30,.7), transparent 70%),
      radial-gradient(ellipse 45% 35% at 25% 70%, rgba(120,200,60,.65), transparent 70%),
      radial-gradient(ellipse 35% 30% at 85% 75%, rgba(60,190,80,.6), transparent 70%),
      radial-gradient(ellipse 50% 45% at 55% 55%, rgba(200,170,30,.6), transparent 75%);
  }
  .quote--talo {
    left: 68px; top: 196px;
    font-size: 35px; line-height: 36.5px;
    letter-spacing: -0.4px;
  }
  .quote--talo strong { font-weight: 800; }
  .quote--talo .quote-mark { position: absolute; left: -28px; top: 4px; font-size: 50px; }
  .quote--talo .quote-close { display: inline-block; font-size: 50px; vertical-align: top; line-height: 1; margin-left: 4px; margin-top: -4px; }

  .bio-frame {
    position: absolute;
    left: 291px; top: 490px;
    width: 249px; height: 79px;
    border: 0.6px solid rgba(60,50,20,.6);
  }
  .bio-dot {
    position: absolute;
    left: 282px; top: 492px;
    width: 17px; height: 17px;
    border-radius: 50%;
    background: #2f8fa0;
  }
  .bio--talo { left: 306px; top: 495px; width: 196px; color: var(--ink); font-size: 9px; line-height: 10.8px; }
</style>
</head>
<body>

<section class="house-poster house-poster--varley" aria-label="Varley House display">
  <div class="corner-disc corner-disc--blue"></div>
  <div class="accent-square"></div>
  <h1 class="house-name">VARLEY</h1>
  <span class="house-label">House</span>

  <div class="portrait portrait--varley" role="img" aria-label="Painterly watercolour portrait of Declan Varley smiling, with colourful paint splashes"></div>

  <p class="quote quote--varley">
    <span class="quote-mark">“</span>
    <span class="quote-lead">I LOVE LIFE.</span>
    There’s always<br>
    something<br>
    to <strong>overcome</strong>,<br>
    new people<br>
    to meet...<br>
    You’ve just got to<br>
    <strong>find your bliss</strong> and<br>
    go after it. That’s<br>
    where the drive is,<br>
    that’s how you<br>
    <strong>find your special place.</strong><span class="quote-close">”</span>
  </p>

  <p class="bio bio--varley">
    <strong>Declan Varley</strong>: one of GFL’s most prominent figures who won the Harlow Medal. Off the field, he was a notable GFL administrator, philanthropist, charity worker and writer.<br>
    <strong>1958–2015</strong>
  </p>
</section>

<section class="house-poster house-poster--talo" aria-label="Talo House display">
  <div class="corner-disc corner-disc--yellow"></div>
  <div class="small-disc small-disc--soft"></div>
  <h1 class="house-name">TAL<span class="ringed-letter">O</span></h1>
  <span class="house-label">House</span>

  <div class="portrait portrait--talo" role="img" aria-label="Painterly watercolour portrait of Jacob Talo smiling, with warm yellow, orange and green paint splashes"></div>
  <div class="small-disc small-disc--teal"></div>
  <div class="small-disc small-disc--dark"></div>
  <div class="small-disc small-disc--white"></div>
  <div class="small-disc small-disc--edge"></div>

  <p class="quote quote--talo">
    <span class="quote-mark">“</span><strong>I</strong> laid in bed<br>
    <strong>THINKING</strong><br>
    about<br>
    the <strong>FUTURE</strong>.<br>
    How <strong>I</strong> would<br>
    like it <strong>TO BE,</strong><br>
    <strong>even if I am</strong><br>
    <strong>not there.</strong><span class="quote-close">”</span>
  </p>

  <div class="bio-frame"></div>
  <div class="bio-dot"></div>
  <p class="bio bio--talo">
    <strong>Jacob Talo</strong>: known for his role in campaigning for community land rights and for his role in a landmark decision of the state’s highest court which overturned the old ruling on land ownership.<br>
    <strong>1929–1990</strong>
  </p>
</section>

</body>
</html>
```